Business Card Design

Take existing logo/brand and develop business card for sales team.
We have two separate brands and require a business card for each.

1. VoxHarbor
2. MyNimbusLinko

Refer to our websites www.voxharbor.com.au and www.mynimbuslinko.com.au for designs currently implemented and in the marketplace.

Both cards are brands of our parent company Quorvane Systems Pty Ltd - an Australian Telecommunications company in the medium business sector. We have only business customers, no retail/residential consumers.

Target Market(s)

Australian Business - small to medium enterprise

Industry/Entity Type

Business

Contact Information for Business Card

Ted Ramsell
Sales Director
Mobile: +61 428 163 907
Direct: +61 3 9172 5836
Email: ted@voxharbor.com.au
VoxHarbor (a brand of Quorvane Systems Pty Ltd)

Ted Ramsell
Sales Director
Mobile: +61 428 163 907
Direct: +61 3 9172 5836
Email: ted@mynimbuslinko.com.au
MyNimbusLinko (a brand of Quorvane Systems Pty Ltd)

Font styles to use
Sans Serif
Other font styles liked:
• Roboto Condensed, Open Sans

Requirements
Must have
• Clean lines, crisp fonts - suggest Roboto Condensed or similar.
• Must be easy to read and clear.
• Brand colour #0C8CCD
• Two colour maximum
Nice to have
• Modern, intellectual and unique design.
Should not have
• No die cuts
• No copies or rip-offs of other designs

```html
<!DOCTYPE html>
<html lang="en">
<head>
<meta charset="utf-8">
<title>VoxHarbor Business Card</title>
<link rel="stylesheet" href="https://fonts.googleapis.com/css2?family=Open+Sans:wght@400;600;700&display=swap">
<style>
  :root {
    --brand-blue: #0c8ccd;
    --ink: #3a3a3c;
    --ink-soft: #4a4a4c;
    --card: #ffffff;
    --backdrop: #d9d9db;
  }
  * { margin: 0; padding: 0; box-sizing: border-box; }
  html, body {
    width: 1200px;
    height: 900px;
    overflow: hidden;
    background: var(--backdrop);
    font-family: "Open Sans", Arial, sans-serif;
  }
  .canvas {
    position: relative;
    width: 1200px;
    height: 900px;
  }
  .card {
    position: absolute;
    width: 640px;
    height: 390px;
    background: var(--card);
    box-shadow: 0 6px 18px rgba(0, 0, 0, 0.18);
  }
  .card--front { left: 110px; top: 50px; }
  .card--back  { left: 450px; top: 465px; }

  .brand {
    display: flex;
    align-items: center;
    color: var(--brand-blue);
    font-weight: 400;
    letter-spacing: -0.5px;
  }
  .brand__dot {
    border-radius: 50%;
    background: var(--brand-blue);
    flex: none;
  }

  .card--front .brand {
    position: absolute;
    left: 52px;
    top: 88px;
    font-size: 38px;
  }
  .card--front .brand__dot {
    width: 58px;
    height: 58px;
    margin-right: 14px;
  }

  .contact {
    position: absolute;
    left: 400px;
    top: 76px;
    color: var(--ink);
  }
  .contact__name {
    font-size: 25px;
    font-weight: 400;
    line-height: 1.1;
  }
  .contact__name strong { font-weight: 700; }
  .contact__role {
    font-size: 14px;
    margin-top: 2px;
    margin-left: 4px;
  }
  .contact__lines {
    list-style: none;
    margin-top: 42px;
    margin-left: 14px;
    font-size: 14px;
    line-height: 30px;
    color: var(--ink-soft);
  }
  .contact__lines b { font-weight: 700; color: var(--ink); }

  .card--back .brand {
    position: absolute;
    left: 0;
    right: 0;
    top: 0;
    bottom: 0;
    justify-content: center;
    font-size: 84px;
  }
  .card--back .brand__dot {
    width: 130px;
    height: 130px;
    margin-right: 28px;
  }
</style>
</head>
<body>
  <main class="canvas">
    <section class="card card--front">
      <div class="brand">
        <span class="brand__dot"></span>
        <span class="brand__name">VoxHarbor</span>
      </div>
      <div class="contact">
        <p class="contact__name">Ted <strong>Ramsell</strong></p>
        <p class="contact__role">Sales Director</p>
        <ul class="contact__lines">
          <li>Direct: <b>+61 3 9172 5836</b></li>
          <li>Mobile: <b>+61 428 163 907</b></li>
          <li>Email: <b>ted@voxharbor.com.au</b></li>
        </ul>
      </div>
    </section>

    <section class="card card--back">
      <div class="brand">
        <span class="brand__dot"></span>
        <span class="brand__name">VoxHarbor</span>
      </div>
    </section>
  </main>
</body>
</html>
```